Medical Company in need of a Modern Flyer design for new Wound Care clinic.

Tri-Fold modern flyer design for our Woundcare company. Logo and description of services can be found on our website; https://www.corvin-woundcare.com/

```html
<!DOCTYPE html>
<html lang="en">
<head>
<meta charset="utf-8">
<title>Corvin Wound Care – Hyperbaric Oxygen Therapy Tri-Fold</title>
<link href="https://fonts.googleapis.com/css2?family=Montserrat:wght@300;400;500;600;700;800&display=swap" rel="stylesheet">
<style>
:root{
  --gold:#f2bd5b;
  --gold-deep:#c9922e;
  --ink:#222222;
  --dark:#262626;
  --dark-2:#1b1b1b;
  --paper:#ffffff;
  --text:#333333;
  --stage:#3a3a3a;
}
*{box-sizing:border-box;margin:0;padding:0}
html,body{width:1200px;height:2429px;overflow:hidden;background:var(--stage);font-family:'Montserrat',sans-serif;color:var(--text)}
.spread{position:absolute;left:48px;width:1106px;height:721px;overflow:hidden;background:var(--paper);box-shadow:0 6px 18px rgba(0,0,0,.4)}
.spread--outside{top:482px}
.spread--inside{top:1227px;background:var(--dark)}
.spread svg.backdrop{position:absolute;inset:0;width:1106px;height:721px}
.abs{position:absolute}
.heading{font-weight:300;text-transform:uppercase;color:var(--ink);letter-spacing:.5px}
.body-copy{font-size:12px;line-height:19px;font-weight:400;letter-spacing:-.1px}
/* outside */
.wellbeing-title{left:95px;top:115px;font-size:30px;line-height:29px}
.feature{left:95px;width:258px}
.feature h3{font-size:13.5px;font-weight:600;color:var(--gold);margin-bottom:2px;line-height:17px}
.feature p{font-size:10.8px;line-height:15.5px;letter-spacing:-.15px}
.feature-icon{position:absolute;left:-58px;top:-4px;width:46px;height:46px}
.about-title{left:402px;top:58px;font-size:30px}
.about-copy{left:402px;top:102px;width:312px}
.brand{left:737px;top:82px;width:369px;text-align:center;font-size:23px;letter-spacing:5px;font-weight:400;color:var(--ink)}
.brand-mark{display:block;width:14px;height:14px;background:var(--gold);margin:0 auto 12px}
.cover-title{left:737px;top:490px;width:369px;text-align:center;font-size:43px;line-height:41px;font-weight:800;color:var(--gold)}
.band-url{font-size:14px;font-weight:500;color:var(--ink);text-align:center;width:369px}
.contact-name{left:433px;top:470px;width:232px;text-align:center;font-size:34px;font-weight:600;letter-spacing:6px;color:var(--gold)}
.contact-title{left:433px;top:575px;width:232px;font-size:20px;font-weight:700;color:var(--gold);border-bottom:1px solid var(--gold);padding-bottom:2px}
.contact-line{left:402px;color:#fff;display:flex;align-items:flex-start;gap:14px}
.phone{top:610px;font-size:20px;font-weight:700}
.address{top:648px;font-size:13px;line-height:15px;font-weight:400}
/* inside */
.hbo-title{left:520px;top:55px;width:540px;text-align:right;font-size:36px;line-height:40px;color:var(--gold)}
.hbo-copy{left:545px;top:142px;width:515px;text-align:right;color:#f0f0f0;font-size:11.8px;line-height:19px}
.list-head{font-size:19px;font-weight:700;color:var(--gold)}
.arrow-list{list-style:none;font-size:12.2px;color:#eee}
.arrow-list li{position:relative;padding-left:14px;line-height:12px;margin-bottom:11.6px}
.arrow-list li::before{content:"";position:absolute;left:1px;top:1px;border-left:6px solid var(--gold);border-top:5px solid transparent;border-bottom:5px solid transparent}
.treat-list li{margin-bottom:8px}
.services-title{left:33px;top:395px;font-size:30px;line-height:29px}
.services-list{left:33px;top:472px;list-style:none;font-size:12.2px;color:var(--text)}
.services-list li{position:relative;padding-left:19px;margin-bottom:12px;line-height:16px}
.services-list li::before{content:"";position:absolute;left:0;top:3px;width:10px;height:10px;background:var(--gold)}
.plans-box{left:735px;top:257px;width:371px;height:464px;background:var(--paper)}
.plans-title{left:30px;top:30px;font-size:30px;line-height:29px}
.plans-copy{left:30px;top:110px;width:300px}
.plan-badge{position:absolute;height:30px;background:#d9d9d9;border-radius:4px}
.band{position:absolute;top:640px;height:81px;background:var(--gold);display:flex;align-items:center;justify-content:center}
</style>
</head>
<body>

<section class="spread spread--outside">
  <svg class="backdrop" viewBox="0 0 1106 721" aria-hidden="true">
    <defs>
      <linearGradient id="goldGrad" x1="0" y1="1" x2="1" y2="0">
        <stop offset="0" stop-color="#b07a22"/><stop offset=".5" stop-color="#f4c46a"/><stop offset="1" stop-color="#c99030"/>
      </linearGradient>
      <linearGradient id="chamberGrad" x1="0" y1="0" x2="0" y2="1">
        <stop offset="0" stop-color="#e6e6e1"/><stop offset=".55" stop-color="#b9b9b2"/><stop offset=".8" stop-color="#2a2a2a"/><stop offset="1" stop-color="#111"/>
      </linearGradient>
      <linearGradient id="roomGrad" x1="0" y1="0" x2="1" y2="1">
        <stop offset="0" stop-color="#2b2d2e"/><stop offset="1" stop-color="#1a1b1c"/>
      </linearGradient>
    </defs>
    <polygon points="0,0 150,0 0,110" fill="#2a2c2c"/>
    <polygon points="160,0 195,0 0,150 0,125" fill="url(#goldGrad)"/>
    <polygon points="125,50 160,50 0,170 0,145" fill="url(#goldGrad)" opacity=".85"/>
    <polygon points="70,721 737,255 737,721" fill="url(#roomGrad)" role="img" aria-label="Dimly lit clinic waiting room photograph"/>
    <polygon points="30,721 58,721 737,246 737,228" fill="url(#goldGrad)"/>
    <polygon points="0,700 0,690 580,300 585,306" fill="url(#goldGrad)"/>
    <polygon points="180,700 200,700 545,455 545,440" fill="url(#goldGrad)" opacity=".9"/>
    <polygon points="737,255 905,145 1106,250 1106,640 737,640" fill="url(#chamberGrad)" role="img" aria-label="Photograph of a hyperbaric oxygen chamber with a made-up bed"/>
    <polyline points="737,245 905,133 1106,238" fill="none" stroke="#f2bd5b" stroke-width="3"/>
    <rect x="737" y="640" width="369" height="81" fill="#f2bd5b"/>
    <rect x="737" y="634" width="369" height="6" fill="#ffffff"/>
  </svg>

  <h2 class="abs heading wellbeing-title">Caring<br>for your<br>well-being</h2>

  <div class="abs feature" style="top:222px">
    <svg class="feature-icon" viewBox="0 0 46 46" fill="none" stroke="#555" stroke-width="1.4"><rect x="6" y="6" width="24" height="32" rx="2"/><path d="M11 14h14M11 20h14M11 26h9"/><path d="M33 24l8 3v6c0 4-4 7-8 8-4-1-8-4-8-8v-6z"/><path d="M33 29v6M30 32h6"/></svg>
    <h3>Accepted Health Plans</h3>
    <p>We accept most major insurance plans to make your care as accessible and affordable as possible!</p>
  </div>
  <div class="abs feature" style="top:302px">
    <svg class="feature-icon" viewBox="0 0 46 46" fill="none" stroke="#555" stroke-width="1.4"><circle cx="23" cy="24" r="7"/><circle cx="23" cy="24" r="3"/><circle cx="12" cy="9" r="3"/><circle cx="23" cy="7" r="3"/><circle cx="34" cy="9" r="3"/><path d="M7 18c0-3 2-5 5-5s5 2 5 5M18 16c0-3 2-5 5-5s5 2 5 5M29 18c0-3 2-5 5-5s5 2 5 5"/><path d="M6 30a17 17 0 0 0 34 0"/></svg>
    <h3>Expert Medical Team</h3>
    <p>Comprised of highly trained physicians, nurses, and specialists, our team brings years of experience in treating a wide range of complex wounds. With a commitment to innovative treatments and personalized care plans, we work closely with each patient to ensure optimal healing and recovery. Trust our team to provide the expert care you need for lasting results.</p>
  </div>
  <div class="abs feature" style="top:480px;width:222px">
    <svg class="feature-icon" viewBox="0 0 46 46" fill="none" stroke="#555" stroke-width="1.4"><path d="M23 30c-8-5-12-9-12-14a6 6 0 0 1 12-2 6 6 0 0 1 12 2c0 5-4 9-12 14z"/><path d="M23 14v8M19 18h8"/><path d="M4 22l6 12 8 6M42 22l-6 12-8 6"/></svg>
    <h3>Trusted Healthcare Provider</h3>
    <p>We specialize in advanced treatment modalities, using a multi-faceted approach to heal your patient's wound.</p>
  </div>

  <h2 class="abs heading about-title">About Us</h2>
  <div class="abs about-copy body-copy">
    <p>At Corvin Wound Care, we specialize in managing outpatient wound care facilities throughout the Dallas/Fort Worth area. Partnering with hospitals and local rehabilitation units, we deliver the most advanced wound care treatments.</p>
    <p style="margin-top:12px">Our commitment to quality care resonates through our collaboration with small practice family providers, ensuring personalized, effective treatment plans.</p>
  </div>

  <div class="abs contact-name">CORVIN</div>
  <div class="abs contact-title">CONTACT INFO</div>
  <div class="abs contact-line phone">
    <svg width="18" height="18" viewBox="0 0 24 24" fill="#f2bd5b"><path d="M6.6 10.8a15 15 0 0 0 6.6 6.6l2.2-2.2a1 1 0 0 1 1-.25 11.4 11.4 0 0 0 3.6.57 1 1 0 0 1 1 1V20a1 1 0 0 1-1 1A17 17 0 0 1 3 4a1 1 0 0 1 1-1h3.5a1 1 0 0 1 1 1c0 1.25.2 2.45.57 3.57a1 1 0 0 1-.25 1z"/></svg>
    <span>555-014-2290</span>
  </div>
  <div class="abs contact-line address">
    <svg width="16" height="20" viewBox="0 0 24 30" fill="#f2bd5b"><path d="M12 0a10 10 0 0 0-10 10c0 8 10 20 10 20s10-12 10-20A10 10 0 0 0 12 0zm0 14a4 4 0 1 1 0-8 4 4 0 0 1 0 8z"/></svg>
    <span>1280 Harlow Ave Ste 210<br>PMB 400172 Dallas, TX 75201</span>
  </div>

  <div class="abs brand"><span class="brand-mark"></span>CORVIN WOUNDCARE</div>
  <h1 class="abs cover-title">HYPERBARIC<br>OXYGEN<br>THERAPY</h1>
  <div class="band" style="left:737px;width:369px"><span class="band-url">www.corvin-woundcare.com</span></div>
</section>

<section class="spread spread--inside">
  <svg class="backdrop" viewBox="0 0 1106 721" aria-hidden="true">
    <defs>
      <linearGradient id="goldGrad2" x1="0" y1="1" x2="1" y2="0">
        <stop offset="0" stop-color="#b07a22"/><stop offset=".5" stop-color="#f4c46a"/><stop offset="1" stop-color="#c99030"/>
      </linearGradient>
      <linearGradient id="scanGrad" x1="0" y1="0" x2="1" y2="1">
        <stop offset="0" stop-color="#f1f1f1"/><stop offset=".6" stop-color="#d8d8d6"/><stop offset="1" stop-color="#9a9a9a"/>
      </linearGradient>
    </defs>
    <rect x="0" y="0" width="370" height="721" fill="#ffffff"/>
    <polygon points="0,0 600,0 370,255 150,350 0,300" fill="url(#scanGrad)" role="img" aria-label="Photograph of a clinician operating a scanner while a patient lies on the table"/>
    <polyline points="0,305 150,355 370,262" fill="none" stroke="#f2bd5b" stroke-width="3"/>
    <polygon points="610,0 640,0 370,300 340,300" fill="url(#goldGrad2)"/>
    <polygon points="655,0 680,0 400,312 378,312" fill="url(#goldGrad2)" opacity=".85"/>
    <polygon points="370,262 372,330 372,721 370,721" fill="#262626"/>
  </svg>

  <h2 class="abs heading hbo-title" style="color:var(--gold)">Hyperbaric Oxygen<br>Therapy (HBO)</h2>
  <p class="abs hbo-copy">A Cornerstone of Advanced Wound Care Hyperbaric Oxygen Therapy (HBO) is not just a treatment; it's a pivotal part of our comprehensive approach to wound healing at Corvin Wound Care. By delivering pure oxygen in a pressurized chamber, HBO therapy significantly increases the amount of oxygen in the blood, fostering an environment that accelerates the repair and regeneration of wounded tissues.</p>

  <h2 class="abs heading services-title">Our<br>Services</h2>
  <ul class="abs services-list">
    <li>Hyperbaric Oxygen Therapy (HBO):<br>A Cornerstone of Advanced Wound Care</li>
    <li>Debridement</li>
    <li>Advanced Wound Dressings</li>
    <li>Bio-engineered Skin Substitutes</li>
    <li>Compression Therapy and Edema Management</li>
  </ul>
  <div class="band" style="left:0;width:370px"><span class="band-url">www.corvin-woundcare.com</span></div>

  <h3 class="abs list-head" style="left:393px;top:286px">WOUND TYPES</h3>
  <ul class="abs arrow-list" style="left:393px;top:318px;width:160px">
    <li>Atypical Wounds</li><li>Bone Infections</li><li>Burn Wounds</li><li>Chronic Wounds</li>
    <li>Diabetic Ulcers</li><li>Diabetic Wounds</li><li>Non-Healing Surgical Wounds</li>
  </ul>
  <ul class="abs arrow-list" style="left:560px;top:318px;width:160px">
    <li>Infected Wounds</li><li>Pilonidal Cysts</li><li>Pressure Ulcers</li><li>Surgical Wound Complications</li>
    <li>Venous &amp; Arterial Ulcers</li><li>Venous Leg Ulcers</li>
  </ul>
  <h3 class="abs list-head" style="left:393px;top:508px">WOUND TREATMENT</h3>
  <ul class="abs arrow-list treat-list" style="left:393px;top:539px;width:300px">
    <li>Compression Therapy</li><li>Mechanical &amp; Enzymatic Debridement</li><li>Negative Pressure Wound Therapy</li>
    <li>Post-Mohs Surgery</li><li>Tissue Infection Management / Labs</li><li>Total Contact Casting</li>
    <li>Wound Care</li><li>Wound Debridement</li>
  </ul>

  <div class="abs plans-box">
    <h2 class="abs heading plans-title">Accepted<br>Health Plans</h2>
    <p class="abs plans-copy body-copy">At My Site, we accept a variety of health insurance plans to ensure that you receive the care you need. If your current plan is not listed, please get in touch with us so we can explore alternative options that best suit your needs.</p>
    <div class="plan-badge" style="left:32px;top:232px;width:92px"></div>
    <div class="plan-badge" style="left:150px;top:232px;width:70px"></div>
    <div class="plan-badge" style="left:244px;top:238px;width:88px;height:20px"></div>
    <div class="plan-badge" style="left:32px;top:302px;width:96px;height:24px"></div>
    <div class="plan-badge" style="left:152px;top:302px;width:82px;height:24px"></div>
    <div class="band" style="left:0;top:383px;width:371px"><span class="band-url">www.corvin-woundcare.com</span></div>
  </div>
</section>

</body>
</html>
```